Poster for Tradesmen Website

We had a soft launch of our website. The site brings together tradesmen jobseekers and customers to one virtual location. The website serves Australian market. To clearly understand what we mean please visit www.workmeld.com.au. For our future promotional campaign we intend to use poster which we intend to distribute in trade exhibits and in recruitment offices.
Color and Poster Design Content: - Very light blue is the predominant color of the website. The design is not limited on this color. They are free to explore other color if they think that will effectively convey the message of the poster. Presently our website uses images showing tradesmen in action as well as the customers. Designers can use these images or use other image in their design which will best suit their design
Size: - We are looking at poster printed A3 size, but the design should not limit their target size on A3 (it should be versatile, insure that the file format for your design support large-format printing without being pixilated) since we also want it printed in vinyl as stand-alone banner (example: 1200 x 1700 mm approx) that will be used in trade exhibits.
Message of the Poster:
For our first marketing campaign we want to join a trade expo which will be held on the last week of May 2012. For this expo we need a poster and a stand-alone banner to be displayed on our booth. The poster should convey the following message:
a) that a new website has been launched
b) that the website brings together tradesmen, customers and jobseekers to one virtual location
c) that for tradesmen the website is a venue to advertise their business
d) that for customers, it will make the task of finding the right tradies much easier
e) that for jobseekers the site is one way of finding a job by just posting their resume and potential employers can view the summary of their qualification and send notification if they are interested on a particular jobseeker.
Images:
We don't have any other high resolution images Except for the images that we used on our website. We got those images online. Besides, we are not sure what particular image will be appropriate for the poster. As the designer and the creative artist as well, you are free to use whatever images that you think is appropriate for the your design. We think any images (not necessarily tradesmen images) can be used as long as it can strongly convey our message. Again, as the creative artist it is up to you to decide what image is/are appropriate. The only thing we can tell you guys is that we can tell a good/excellent design when we see one.
Logo:
We don't have a logo yet for our website. For the purpose of this poster you can use the font used on website name:
workmeld.com.au
tradie {font-family:Arial, Helvetica, sans-serif; color:#407FC0;}
meld.com.au {font-family:Arial, Helvetica, sans-serif; color:#00007F;}
Target Market(s)
Age group: 18 - 65, Gender: male-female, Education: any
Industry/Entity Type
Marketing
Look and feel
Each slider illustrates characteristics of the customer's brand and the style your logo design should communicate.

```html
<!DOCTYPE html>
<html lang="en">
<head>
<meta charset="utf-8">
<title>WorkMeld – One Stop Solution for Tradesmen/Businesses</title>
<link rel="stylesheet" href="https://fonts.googleapis.com/css2?family=Noto+Serif:wght@700&family=Oswald:wght@500&family=Arimo:wght@400;700&display=swap">
<style>
  :root {
    --navy: #0b1c86;
    --royal: #1c3fae;
    --sky: #4a8de0;
    --pale: #e9ecf2;
    --paper: #eef0f3;
    --white: #ffffff;
    --ink: #111111;
    --bullet-text: #3b7dd6;
  }
  * { margin: 0; padding: 0; box-sizing: border-box; }
  html, body { width: 848px; height: 1200px; overflow: hidden; background: var(--paper); }
  .poster { position: relative; width: 848px; height: 1200px; overflow: hidden; background: var(--paper); font-family: "Arimo", Arial, sans-serif; }
  .backdrop { position: absolute; inset: 0; }
  .headline {
    position: absolute; top: 26px; left: 40px; width: 500px;
    font-family: "Noto Serif", Georgia, serif; font-weight: 700;
    font-size: 33px; line-height: 42px; color: var(--sky); text-align: center;
  }
  .offers {
    position: absolute; top: 152px; left: 90px; width: 410px;
    font-family: "Oswald", "Arial Narrow", sans-serif; font-weight: 500;
    font-size: 30px; line-height: 44px; color: var(--white); text-align: center;
    letter-spacing: 0.5px;
  }
  .logon {
    position: absolute; left: 155px; top: 352px;
    font-size: 21px; color: #dfe8fb; letter-spacing: 1px;
    transform: rotate(-10deg); transform-origin: left bottom;
  }
  .site-url {
    position: absolute; left: 34px; top: 442px; white-space: nowrap;
    color: var(--navy); transform: rotate(-10deg); transform-origin: left bottom;
  }
  .site-url .prefix { font-size: 26px; }
  .site-url .domain { font-size: 38px; font-weight: 700; }
  .photo {
    position: absolute; border: 7px solid var(--white);
    box-shadow: 0 2px 6px rgba(0,0,0,0.35);
  }
  .photo-crew {
    left: 535px; top: 18px; width: 240px; height: 345px; border: none; box-shadow: none;
    background: linear-gradient(180deg, #e9edf4 0%, #3f4f87 45%, #2d3a6a 100%);
    border-radius: 40px 40px 6px 6px; opacity: 0.9;
  }
  .photo-welder {
    left: 82px; top: 539px; width: 305px; height: 198px;
    transform: rotate(-16deg);
    background: linear-gradient(135deg, #6f9fd8 0%, #5a4a3a 45%, #2a2a2f 100%);
  }
  .photo-plumber {
    left: 545px; top: 835px; width: 295px; height: 221px;
    transform: rotate(14deg);
    background: linear-gradient(135deg, #c9ccd2 0%, #8a8f98 40%, #d8b690 100%);
  }
  .cursor { position: absolute; left: 0; top: 0; }
  .click-here {
    position: absolute; left: 500px; top: 540px;
    font-weight: 700; font-size: 19px; color: var(--navy);
    transform: rotate(-56deg); white-space: nowrap;
  }
  .features-title {
    position: absolute; left: 55px; top: 825px;
    font-family: "Oswald", "Arial Narrow", sans-serif; font-weight: 500;
    font-size: 22px; color: var(--navy); letter-spacing: 0.3px;
  }
  .features { position: absolute; left: 55px; top: 898px; list-style: none; }
  .features li { display: flex; align-items: center; height: 34px; font-size: 12.5px; color: var(--bullet-text); }
  .features li::before { content: ""; width: 45px; height: 11px; background: var(--navy); margin-right: 8px; }
  .contact { position: absolute; left: 23px; top: 1046px; color: var(--white); font-weight: 700; }
  .contact .label { font-size: 29px; line-height: 36px; letter-spacing: 0.5px; }
  .contact .phone { font-size: 29px; line-height: 36px; letter-spacing: 1px; }
  .footer-url { position: absolute; left: 23px; top: 1140px; color: var(--white); font-weight: 700; font-size: 28px; letter-spacing: 0.5px; }
</style>
</head>
<body>
<main class="poster">
  <svg class="backdrop" width="848" height="1200" viewBox="0 0 848 1200" aria-hidden="true">
    <defs>
      <linearGradient id="band" x1="0" y1="0" x2="1" y2="0">
        <stop offset="0" stop-color="#0b1c86"/>
        <stop offset="0.55" stop-color="#2447b6"/>
        <stop offset="1" stop-color="#1a3aa8"/>
      </linearGradient>
      <linearGradient id="stripe" x1="0" y1="0" x2="0" y2="1">
        <stop offset="0" stop-color="#ffffff"/>
        <stop offset="1" stop-color="#d5e2fa"/>
      </linearGradient>
      <linearGradient id="lower" x1="0" y1="0" x2="1" y2="0">
        <stop offset="0" stop-color="#7ea5ea"/>
        <stop offset="1" stop-color="#e8eef9"/>
      </linearGradient>
      <linearGradient id="wave" x1="0" y1="0" x2="1" y2="1">
        <stop offset="0" stop-color="#1f46c4"/>
        <stop offset="1" stop-color="#0b1c86"/>
      </linearGradient>
      <radialGradient id="glow" cx="0.45" cy="0.5" r="0.5">
        <stop offset="0" stop-color="#ffffff"/>
        <stop offset="1" stop-color="#e6e8ec"/>
      </radialGradient>
    </defs>
    <rect x="0" y="0" width="848" height="134" fill="url(#glow)"/>
    <polygon points="0,134 848,134 848,310 0,690" fill="url(#band)"/>
    <polygon points="0,440 848,275 848,345 0,575" fill="url(#stripe)"/>
    <polygon points="0,575 848,345 848,375 0,650" fill="url(#lower)"/>
    <path d="M0,1005 C180,990 360,1060 520,1090 C650,1115 760,1110 848,1095 L848,1200 L0,1200 Z" fill="url(#wave)"/>
    <path d="M0,1005 C180,990 360,1060 520,1090 C650,1115 760,1110 848,1095" fill="none" stroke="#5b86e6" stroke-width="3"/>
  </svg>

  <h1 class="headline">One Stop Solution for Tradesmen/Businesses</h1>

  <div class="photo photo-crew" role="img" aria-label="Two smiling tradesmen in work clothes holding a plunger and a wrench"></div>

  <p class="offers">ADVERTISE YOUR BUSINESS<br>ADVERTISE YOUR PROJECT<br>POST YOUR RESUME</p>

  <p class="logon">JUST LOGON TO</p>
  <p class="site-url"><span class="prefix">http://www.</span><span class="domain">workmeld.com.au</span></p>

  <div class="photo photo-welder" role="img" aria-label="Welder in a protective mask working on a steel pipe"></div>

  <svg class="cursor" width="848" height="1200" viewBox="0 0 848 1200" aria-hidden="true">
    <defs>
      <linearGradient id="arrowFill" x1="0" y1="0" x2="1" y2="1">
        <stop offset="0" stop-color="#ffffff"/>
        <stop offset="1" stop-color="#a9c4f2"/>
      </linearGradient>
    </defs>
    <polygon points="420,433 724,512 627,562 765,668 710,719 595,613 549,738" fill="url(#arrowFill)" stroke="var(--ink)" stroke-width="8" stroke-linejoin="miter"/>
  </svg>
  <p class="click-here">CLICK HERE</p>

  <h2 class="features-title">NAM RISUS QUAM, COMMODO EU TRISTIQUE NEC</h2>
  <ul class="features">
    <li>Maecenas tempor massa ac nisi vestibulum et aliquam ante.</li>
    <li>Maecenas tempor massa ac nisi vestibulum et aliquam ante.</li>
    <li>Maecenas tempor massa ac nisi vestibulum et aliquam ante.</li>
  </ul>

  <div class="photo photo-plumber" role="img" aria-label="Plumber repairing pipes under a kitchen sink while a customer watches"></div>

  <div class="contact">
    <p class="label">CALL US ON:</p>
    <p class="phone">123 456 789</p>
  </div>
  <p class="footer-url">http://www.workmeld.com.au</p>
</main>
</body>
</html>
```